Professional Business Cards

We need a nice looking, profession and modern business card for our new company. Our logo is attatched

Target Market(s)

Young Professionals

Industry/Entity Type

Financial

Contact Information for Business Card

FRONT

Morvane Tally Pty Ltd
Level 22, Halden Court, 48 Wirrapool St
Sydney NSW 2000
ABN : 57 304 918 226

Derek Wallis - Chief Operations Officer
P : 02 7153 2819
M: 0418 395 207
derek@morvanetally,com

BACK

- Cryptocurrency Exchange Services
- Cryptocurrency Mining Operations
- Cryptocurrency Investment Fund Offering

Font styles to use
Sans Serif

Colors
0255a3
9d9d9d

```html
<!DOCTYPE html>
<html lang="en">
<head>
<meta charset="utf-8">
<title>Morvane Tally – Business Cards</title>
<link href="https://fonts.googleapis.com/css2?family=Open+Sans:wght@400;600;700&display=swap" rel="stylesheet">
<style>
  :root {
    --brand-blue: #0255a3;
    --brand-grey: #9d9d9d;
    --text-grey: #6b6b6b;
    --dark-grey: #555555;
    --card-white: #ffffff;
    --canvas-bg: #e9eaec;
    --pale-blue: #e3ebf4;
  }
  * { margin: 0; padding: 0; box-sizing: border-box; }
  html, body {
    width: 1200px; height: 900px; overflow: hidden;
    background: var(--canvas-bg);
    font-family: "Open Sans", sans-serif;
  }
  .canvas {
    position: relative; width: 1200px; height: 900px;
  }
  .card {
    position: absolute; left: 255px;
    width: 690px; height: 395px;
    background: var(--card-white);
    overflow: hidden;
    box-shadow: 0 6px 18px rgba(0,0,0,0.12);
  }
  .card--back { top: 40px; }
  .card--front { top: 465px; }

  .bands { position: absolute; inset: 0; }

  .brand {
    position: absolute;
    display: flex; align-items: center; gap: 12px;
  }
  .brand__square {
    width: 26px; height: 26px; background: var(--brand-blue);
  }
  .brand__name {
    font-weight: 700; color: var(--brand-blue);
    text-transform: uppercase; letter-spacing: 1px;
    font-size: 34px; line-height: 1;
  }
  .card--back .brand { right: 50px; top: 70px; }

  .services {
    position: absolute; right: 50px; top: 140px;
    list-style: none; text-align: right;
    color: var(--dark-grey); font-size: 16px; line-height: 1.45;
  }
  .services li::before { content: "• "; }

  .card--front .brand { right: 45px; top: 40px; }
  .card--front .brand__name { font-size: 30px; }
  .abn {
    position: absolute; right: 45px; top: 84px;
    font-size: 11px; color: var(--text-grey); letter-spacing: 0.3px;
  }

  .person { position: absolute; left: 50px; top: 100px; }
  .person__name {
    font-weight: 700; color: var(--brand-blue);
    font-size: 19px; text-transform: uppercase; letter-spacing: 0.3px;
  }
  .person__title { color: var(--text-grey); font-size: 18px; }

  .address {
    position: absolute; right: 45px; top: 165px;
    text-align: right; color: var(--text-grey);
    font-size: 18px; line-height: 1.3;
  }
  .address__company { font-weight: 700; }

  .contact {
    position: absolute; left: 50px; bottom: 36px;
    list-style: none; color: var(--text-grey);
    font-size: 18px; line-height: 1.3;
  }
  .contact__label {
    display: inline-block; width: 26px;
    color: var(--brand-blue); font-weight: 400;
  }
</style>
</head>
<body>
<main class="canvas">

  <section class="card card--back" aria-label="Card back">
    <svg class="bands" width="690" height="395" viewBox="0 0 690 395" aria-hidden="true">
      <polygon points="110,0 175,0 0,250 0,157" fill="var(--brand-blue)"/>
      <polygon points="30,395 120,395 0,300 0,372" fill="var(--brand-blue)" opacity="0"/>
      <polygon points="0,330 300,395 210,395 0,350" fill="var(--brand-blue)" opacity="0"/>
      <polygon points="0,300 0,345 215,395 310,395" fill="var(--brand-blue)"/>
    </svg>
    <div class="brand">
      <span class="brand__square"></span>
      <span class="brand__name">Morvane Tally</span>
    </div>
    <ul class="services">
      <li>Cryptocurrency Exchange Services</li>
      <li>Cryptocurrency Mining Operations</li>
      <li>Cryptocurrency Investment Fund Offering</li>
    </ul>
  </section>

  <section class="card card--front" aria-label="Card front">
    <svg class="bands" width="690" height="395" viewBox="0 0 690 395" aria-hidden="true">
      <polygon points="80,0 160,0 0,200 0,100" fill="var(--pale-blue)"/>
      <polygon points="0,300 0,345 215,395 310,395" fill="var(--pale-blue)"/>
    </svg>
    <div class="brand">
      <span class="brand__square"></span>
      <span class="brand__name">Morvane Tally</span>
    </div>
    <p class="abn">ABN : 57 304 918 226</p>

    <div class="person">
      <p class="person__name">Derek Wallis</p>
      <p class="person__title">Chief Operations Officer</p>
    </div>

    <address class="address" style="font-style: normal;">
      <span class="address__company">Morvane Tally Pty Ltd</span><br>
      Level 22, Halden Court<br>
      48 Wirrapool St<br>
      Sydney NSW 2000
    </address>

    <ul class="contact">
      <li><span class="contact__label">P</span>02 7153 2819</li>
      <li><span class="contact__label">M</span>0418 395 207</li>
      <li><span class="contact__label">E</span>derek@morvanetally.com</li>
      <li><span class="contact__label">W</span>www.morvanetally.com</li>
    </ul>
  </section>

</main>
</body>
</html>
```